Web Design Project

We need a web design for a new business in Orland Park, IL.
We are a restaurant meal delivery business. We deliver from a variety of restaurants. We gives our customers an alternative to just pizza delivery.

Websites we like:
http://www.brambleporter.example/
https://www.quillfetchgo.example/Default.asp
www.wendlerunner.example/

Our current website is www.tovenbasket.example(not to be used as a guide, i'm looking for an original design)
Updates

Please no pictures of anything associated with Pizza.  We are a restaurant delivery business that gives our customers an alternative to just pizza delivery. 

This is my original logo.  I uploaded the file to the job brief and updated the brief some.

Target Market(s)

Two income households with children.

Industry/Entity Type

Business

Requirements
Must have
• Order Now button,and sliding photographs of food.
Nice to have
• a background other than white(it can be white if it works with the design)
Should not have
• A picture of pizza that cant be changed. It is ok if the photo is apart of sliding photo's, but pizza cant be the main focus of our delivery service.

```html
<!DOCTYPE html>
<html lang="en">
<head>
<meta charset="utf-8">
<title>Toven Basket – Restaurant Delivery</title>
<link href="https://fonts.googleapis.com/css2?family=Open+Sans:wght@300;400;600;700&family=Open+Sans+Condensed:wght@300;700&display=swap" rel="stylesheet">
<style>
:root{
  --red:#c40000;
  --red-dark:#9e0000;
  --nav-dark:#262626;
  --text:#555555;
  --heading:#555555;
  --grey-footer:#8c8c8c;
  --grey-footer-dark:#7d7d7d;
  --sky:#dfeaf3;
  --white:#ffffff;
}
*{box-sizing:border-box;margin:0;padding:0}
html,body{width:1200px;height:900px;overflow:hidden}
body{
  position:relative;
  font-family:"Open Sans",Arial,sans-serif;
  color:var(--text);
  background:
    radial-gradient(ellipse 700px 380px at 150px 60px,var(--sky),rgba(255,255,255,0) 70%),
    radial-gradient(ellipse 500px 300px at 1100px 120px,#eaf1f6,rgba(255,255,255,0) 70%),
    var(--white);
}
.brand{position:absolute;left:234px;top:40px;width:140px;display:flex;align-items:center;gap:7px;white-space:nowrap}
.brand-dot{flex:none;width:22px;height:22px;border-radius:50%;background:var(--red)}
.brand-name{font-family:"Open Sans Condensed",Arial,sans-serif;font-weight:700;font-size:20px;color:var(--red);line-height:1}

.main-nav{
  position:absolute;left:383px;top:33px;width:817px;height:43px;
  background:linear-gradient(#3d3d3d,var(--nav-dark));
  border-radius:4px 0 0 4px;
  box-shadow:0 2px 4px rgba(0,0,0,.35);
}
.main-nav ul{list-style:none;display:flex;height:100%;padding-left:14px}
.main-nav li{
  font-family:"Open Sans Condensed",Arial,sans-serif;font-weight:700;font-size:12px;
  color:#d2d2d2;padding:0 8px;line-height:43px;text-transform:uppercase;white-space:nowrap;
}
.main-nav li.home{color:var(--white)}
.main-nav li.active{
  background:linear-gradient(#e01818,var(--red-dark));color:var(--white);
  height:38px;line-height:40px;border-radius:0 0 3px 3px;padding:0 10px;
  box-shadow:0 2px 3px rgba(0,0,0,.3);
}

.hero-scene{
  position:absolute;left:245px;top:76px;width:715px;height:270px;
  background:
    radial-gradient(ellipse 230px 90px at 250px 210px,#5d8f3a,rgba(93,143,58,0) 70%),
    radial-gradient(ellipse 180px 120px at 440px 90px,#f3f5f6,rgba(243,245,246,0) 70%),
    linear-gradient(180deg,#b9c8d6 0%,#8ea1b4 40%,#6b8a5a 75%,#3a3a3a 92%,rgba(255,255,255,0) 100%);
  border-radius:0 0 340px 340px / 0 0 60px 60px;
  clip-path:polygon(0 0,100% 0,100% 74%,78% 74%,78% 100%,0 100%);
  opacity:.85;
}
.order-box{
  position:absolute;left:287px;top:110px;width:193px;height:162px;
  background:rgba(245,245,245,.95);border-radius:4px;
  box-shadow:0 2px 10px rgba(0,0,0,.15);padding:14px 14px 0 14px;
}
.order-box h2{font-weight:400;font-size:18px;color:var(--red);margin-left:6px}
.order-box label{display:block;font-size:13.5px;color:var(--text);margin:14px 0 6px 6px}
.zip-select{
  display:flex;align-items:center;justify-content:space-between;
  width:165px;height:30px;background:var(--white);border:1px solid #cfcfcf;border-radius:3px;
  font-size:13px;color:#333;padding-left:13px;
}
.zip-select .arrow{width:30px;height:100%;border-left:1px solid #ddd;display:flex;align-items:center;justify-content:center}
.btn-dark{
  display:flex;align-items:center;justify-content:center;gap:10px;
  margin-top:10px;width:165px;height:30px;border-radius:3px;
  background:linear-gradient(#3b3b3b,#1c1c1c);color:var(--white);
  font-family:"Open Sans Condensed",Arial,sans-serif;font-weight:700;font-size:13px;
}

.my-order{position:absolute;right:264px;top:291px;text-align:right;font-size:11px;line-height:14px;color:var(--text)}
.my-order strong{display:block;font-weight:400;font-size:14px;line-height:18px;color:var(--red)}
.btn-signin{
  position:absolute;left:856px;top:328px;width:82px;height:30px;border-radius:3px;
  background:linear-gradient(#9a9a9a,#6e6e6e);color:var(--white);
  font-family:"Open Sans Condensed",Arial,sans-serif;font-weight:700;font-size:13px;
  display:flex;align-items:center;justify-content:center;gap:8px;
  box-shadow:0 2px 3px rgba(0,0,0,.3);
}

.section-title{position:absolute;left:260px;font-weight:300;font-size:17.5px;color:var(--heading);white-space:nowrap}
.divider{position:absolute;left:240px;width:721px;height:6px}
.restaurants{position:absolute;left:245px;top:420px;width:710px;height:40px;display:flex;align-items:center;justify-content:space-between;overflow:hidden}
.restaurant{font-family:"Open Sans Condensed",Arial,sans-serif;font-weight:700;font-size:15px;color:#6a6a6a;white-space:nowrap}

.reasons{position:absolute;top:567px;list-style:none}
.reasons li{position:relative;font-size:10.8px;line-height:13px;color:var(--text);margin-bottom:12px;padding-left:22px}
.reasons li::before{
  content:"";position:absolute;left:2px;top:3px;width:4px;height:4px;
  border-right:2px solid #555;border-top:2px solid #555;transform:rotate(45deg);
}
.reasons.left{left:270px;width:305px}
.reasons.right{left:630px;width:315px}

.footer-links{
  position:absolute;left:0;top:750px;width:1200px;height:46px;background:var(--red);
  display:flex;align-items:center;padding-left:265px;
  font-size:9px;color:#f3caca;white-space:nowrap;
}
.footer-links span.sep{margin:0 5px;color:#f3caca}
.footer-links .current{color:var(--white);font-weight:700;text-decoration:underline}
.footer-base{
  position:absolute;left:0;top:796px;width:1200px;height:104px;
  background:repeating-linear-gradient(45deg,var(--grey-footer) 0 2px,var(--grey-footer-dark) 2px 4px);
}
.copyright{position:absolute;left:263px;top:821px;font-size:9.5px;color:#f2f2f2}
.social{position:absolute;left:761px;top:815px;display:flex;gap:6px}
.social span{width:24px;height:24px;border-radius:3px;background:linear-gradient(#5a5a5a,#3c3c3c);box-shadow:0 1px 2px rgba(0,0,0,.35)}
</style>
</head>
<body>

<header>
  <div class="brand"><span class="brand-dot"></span><span class="brand-name">Toven Basket</span></div>
  <nav class="main-nav">
    <ul>
      <li class="home">Home</li>
      <li>Restaurants</li>
      <li>How do I order?</li>
      <li class="active">Corporate</li>
      <li>Gift Certificate</li>
      <li>About Us</li>
      <li>Contact Us</li>
      <li>Comments</li>
    </ul>
  </nav>
</header>

<section class="hero">
  <div class="hero-scene" role="img" aria-label="Delivery van driving on a curved road around a green park island with city skyscrapers behind"></div>
  <form class="order-box">
    <h2>Ready to Order?</h2>
    <label>Select your ZIP Code:</label>
    <div class="zip-select">60467
      <span class="arrow"><svg width="9" height="6" viewBox="0 0 9 6"><path d="M1 1l3.5 3.5L8 1" fill="none" stroke="#555" stroke-width="1.8"/></svg></span>
    </div>
    <div class="btn-dark">START YOUR ORDER <svg width="7" height="11" viewBox="0 0 7 11"><path d="M1 1l4.5 4.5L1 10" fill="none" stroke="#888" stroke-width="2"/></svg></div>
  </form>
  <div class="my-order">My Order:<strong>No Orders</strong></div>
  <div class="btn-signin">SIGN IN <svg width="7" height="11" viewBox="0 0 7 11"><path d="M1 1l4.5 4.5L1 10" fill="none" stroke="#ddd" stroke-width="2"/></svg></div>
</section>

<section>
  <h3 class="section-title" style="top:367px">Best restaurants</h3>
  <svg class="divider" style="top:397px" viewBox="0 0 721 6"><circle cx="3" cy="3" r="2.5" fill="none" stroke="#777"/><line x1="6" y1="3" x2="715" y2="3" stroke="#999" stroke-width="2" stroke-dasharray="2 1"/><circle cx="718" cy="3" r="2.5" fill="none" stroke="#777"/></svg>
  <div class="restaurants">
    <span class="restaurant">Hatfield Pies</span>
    <span class="restaurant">Kilnhouse</span>
    <span class="restaurant">Brisko</span>
    <span class="restaurant">Lantern Wok</span>
    <span class="restaurant">Orbit Slice</span>
    <span class="restaurant">Nonna Vee</span>
    <span class="restaurant">Amalto</span>
    <span class="restaurant">Longroll</span>
  </div>
</section>

<section>
  <h3 class="section-title" style="top:510px">Why our customers order through us?</h3>
  <svg class="divider" style="top:540px" viewBox="0 0 721 6"><circle cx="3" cy="3" r="2.5" fill="none" stroke="#777"/><line x1="6" y1="3" x2="715" y2="3" stroke="#999" stroke-width="2" stroke-dasharray="2 1"/><circle cx="718" cy="3" r="2.5" fill="none" stroke="#777"/></svg>
  <ul class="reasons left">
    <li>We make your life easier by delivering quality restaurant food to your home, office or hotel.</li>
    <li>You don't have to worry about cooking or cleaning.</li>
    <li>We provide the highest quality food from the areas' best restaurants.</li>
    <li>We make it easy to cater parties and business functions by delivering everything that you need, including: plates, napkins, utensils, serving pieces, cups, ice, beverages and dessert.</li>
  </ul>
  <ul class="reasons right">
    <li>You can order in advance and have your meal delivered at a specified date and time.</li>
    <li>We ensure that your food is served fresh by utilizing specially designed food containers in our vehicles.</li>
    <li>The food containers keep the food at the correct temperature until it is delivered to you.</li>
  </ul>
</section>

<footer>
  <div class="footer-links">
    <span>Home</span><span class="sep">|</span>
    <span class="current">Restaurants</span><span class="sep">|</span>
    <span>How Do I Order?</span><span class="sep">|</span>
    <span>Corporate Account Signup</span><span class="sep">|</span>
    <span>Gift Certificate</span><span class="sep">|</span>
    <span>About Us</span><span class="sep">|</span>
    <span>Contact Us</span><span class="sep">|</span>
    <span>Comments</span><span class="sep">|</span>
    <span>FAQ</span><span class="sep">|</span>
    <span>Privacy Policy</span><span class="sep">|</span>
    <span>Site Map</span>
  </div>
  <div class="footer-base"></div>
  <p class="copyright">Copyright © 2013 Toven Basket</p>
  <div class="social"><span></span><span></span><span></span><span></span><span></span><span></span></div>
</footer>

</body>
</html>
```